Design for schnapps bottle label "Sol Terrado"

Hi! On a small land lot we are producing our own Italian schnapps "Grappa". For the bottles we would like to modernize our current labes that you find below. The two cats looking at each other should remain, but updated and more modern. I am very much looking forward to your suggestions. Best, Joel

Target Market(s)

Schnapps bottle label

Requirements
Must have
• Cats should resemble the cats that are decorating the house entry (see attached), however, should have a more modern appearance.

Text elements should remain: "Grappa", "Sol Terrado", "Legnoso", "[Vintage Year], "Raccolta No", "Vol %"
Should not have
• Current ornament can be used, replaced or deleted (whatever looks best)

```html
<!DOCTYPE html>
<html lang="en">
<head>
<meta charset="utf-8">
<title>Grappa Legnoso – Sol Terrado label</title>
<link rel="stylesheet" href="https://fonts.googleapis.com/css2?family=Federo&display=swap">
<style>
  :root {
    --page: #e8e6e3;
    --label-deep: #0d2426;
    --label-mid: #173a3d;
    --gold: #e8c96c;
    --gold-soft: #c9a752;
    --gold-faint: rgba(232, 201, 108, 0.28);
  }
  * { margin: 0; padding: 0; box-sizing: border-box; }
  html, body { width: 1200px; height: 960px; overflow: hidden; background: var(--page); }
  .canvas { position: relative; width: 1200px; height: 960px; }
  .label {
    position: absolute; left: 341px; top: 40px; width: 517px; height: 880px;
    background: radial-gradient(ellipse at 50% 45%, var(--label-mid), var(--label-deep) 80%);
    color: var(--gold); font-family: "Federo", sans-serif; overflow: hidden;
  }
  .ornament {
    position: absolute; left: 180px; top: 34px; width: 290px; height: 36px;
    background: var(--gold-faint); border-radius: 4px;
  }
  .product-name {
    position: absolute; left: 0; right: 0; top: 76px; text-align: center;
    font-size: 132px; font-weight: 400; line-height: 1; letter-spacing: 0;
  }
  .title-rule { position: absolute; left: 50px; top: 222px; width: 417px; height: 2px; background: var(--gold); }
  .style-line { position: absolute; left: 0; right: 0; top: 300px; text-align: center; font-size: 50px; line-height: 1.2; }
  .connector { position: absolute; left: 0; right: 0; top: 388px; text-align: center; font-size: 46px; line-height: 1.2; }
  .cat {
    position: absolute; top: 460px; height: 206px;
    background: linear-gradient(160deg, var(--gold), var(--gold-soft)); opacity: 0.85; border-radius: 40px 40px 12px 12px;
  }
  .cat-left { left: 73px; width: 176px; }
  .cat-right { left: 303px; width: 150px; }
  .maker { position: absolute; left: 0; right: 0; top: 680px; text-align: center; font-size: 52px; line-height: 1.2; letter-spacing: 3px; }
  .batch, .strength { position: absolute; top: 832px; font-size: 24px; line-height: 1.2; }
  .batch { left: 8px; }
  .strength { right: 8px; }
</style>
</head>
<body>
<div class="canvas">
  <div class="label">
    <div class="ornament" role="img" aria-label="Gold decorative flourish above the product name"></div>
    <h1 class="product-name">Grappa</h1>
    <div class="title-rule"></div>
    <p class="style-line">“legnoso” 2015</p>
    <p class="connector">di</p>
    <div class="cat cat-left" role="img" aria-label="Gold silhouette of a stretching cat facing right"></div>
    <div class="cat cat-right" role="img" aria-label="Gold silhouette of a stretching cat facing left"></div>
    <p class="maker">Sol Terrado</p>
    <p class="batch">Raccolta No. 01</p>
    <p class="strength">41.0% Vol</p>
  </div>
</div>
</body>
</html>
```